A5 Personal trainer profile for corbell vitality

I need a A5 Landscape profile designed for the company I work for. Company name is Corbell Vitality. The profile is for personal trainers to let people know:

1. Brief description of themselves
2. Qualifications

A picture will be required on the right hand side of the profile. Corbell Vitality colours are green and white.

The Corbell Vitality Logo in the boarder of the example included must remain. We are looking for a clinical and professional design.

Industry/Entity Type

Health

```html
<!DOCTYPE html>
<html lang="en">
<head>
<meta charset="utf-8">
<title>Personal Trainer Profile – Marcus Ofori – Corbell Vitality</title>
<link href="https://fonts.googleapis.com/css2?family=Bebas+Neue&family=Lato:wght@400;700&family=Montserrat:wght@800&display=swap" rel="stylesheet">
<style>
  :root {
    --backdrop: #1c1c1c;
    --green-deep: #0f5f2c;
    --green-mid: #1f8a3c;
    --green-bright: #46b649;
    --green-brand: #3aa645;
    --photo-tone: #b9e47c;
    --white: #ffffff;
  }
  * { margin: 0; padding: 0; box-sizing: border-box; }
  html, body {
    width: 1200px; height: 999px; overflow: hidden;
    background: var(--backdrop);
  }
  .profile-card {
    position: absolute; left: 80px; top: 133px;
    width: 1040px; height: 733px;
    background: var(--white);
    color: var(--white);
    font-family: "Lato", Arial, sans-serif;
  }
  .card-shapes, .trainer-photo { position: absolute; left: 0; top: 0; }
  .role-title {
    position: absolute; left: 38px; top: 12px;
    font-family: "Montserrat", Arial, sans-serif; font-weight: 800;
    font-size: 46px; letter-spacing: 1.5px; line-height: 1.2;
    text-shadow: 0 2px 4px rgba(0,0,0,0.35);
  }
  .trainer-name {
    position: absolute; left: 37px; top: 62px;
    font-family: "Bebas Neue", Impact, sans-serif;
    font-size: 112px; line-height: 1; letter-spacing: 0;
    text-shadow: 0 3px 5px rgba(0,0,0,0.35);
  }
  .section-heading {
    position: absolute;
    font-family: "Bebas Neue", Impact, sans-serif;
    font-size: 44px; line-height: 1; letter-spacing: 0.3px;
  }
  .help-heading { left: 28px; top: 190px; word-spacing: -3px; }
  .clients-heading { left: 25px; top: 376px; font-size: 45px; }
  .qualifications-heading { left: 36px; top: 574px; }
  .service-list {
    position: absolute; left: 30px; top: 234px;
    list-style: none; font-size: 19.5px; line-height: 25px;
  }
  .service-list li { display: flex; }
  .service-list .arrow { width: 47px; font-weight: 700; font-size: 17px; }
  .client-quote {
    position: absolute; left: 22px; top: 418px; width: 490px;
    font-size: 19.5px; line-height: 25px;
  }
  .qualification-list {
    position: absolute; left: 34px; top: 614px;
    list-style: none; font-size: 19.8px; line-height: 25px;
  }
  .qualification-list li { display: flex; align-items: baseline; }
  .qualification-list .dot { width: 64px; font-size: 12px; }
  .brand-mark {
    position: absolute; left: 520px; top: 506px;
    display: flex; align-items: center; gap: 14px;
    font-family: "Lato", Arial, sans-serif; font-weight: 700;
    font-size: 48px; line-height: 1; color: var(--green-brand);
  }
  .brand-square {
    width: 36px; height: 36px; background: var(--green-brand);
  }
</style>
</head>
<body>
  <section class="profile-card">
    <svg class="card-shapes" width="1040" height="733" viewBox="0 0 1040 733" aria-hidden="true">
      <defs>
        <linearGradient id="panelGradient" x1="0" x2="1" y1="0" y2="0">
          <stop offset="0" stop-color="var(--green-deep)"/>
          <stop offset="0.6" stop-color="var(--green-mid)"/>
          <stop offset="1" stop-color="var(--green-bright)"/>
        </linearGradient>
        <linearGradient id="bandGradient" x1="0" x2="1" y1="0" y2="0">
          <stop offset="0" stop-color="var(--green-deep)"/>
          <stop offset="0.5" stop-color="var(--green-mid)"/>
          <stop offset="0.9" stop-color="var(--green-bright)"/>
        </linearGradient>
      </defs>
      <polygon class="intro-panel" points="0,0 655,0 489,557 0,557" fill="url(#panelGradient)"/>
      <polygon class="header-panel" points="0,0 655,0 605,170 0,170" fill="var(--green-deep)"/>
      <polygon class="right-edge" points="1040,285 1040,557 1008,557" fill="var(--green-bright)"/>
      <polygon class="qualifications-band" points="0,561 966,561 918,733 0,733" fill="url(#bandGradient)"/>
      <polygon class="corner-panel" points="975,561 1040,561 1040,733 927,733" fill="var(--green-deep)"/>
    </svg>

    <svg class="trainer-photo" width="1040" height="733" viewBox="0 0 1040 733" role="img" aria-label="Portrait photo of the personal trainer in a green polo shirt">
      <polygon points="668,0 1040,0 1040,262 1002,557 503,557" fill="var(--photo-tone)"/>
    </svg>

    <svg class="card-shapes" width="1040" height="733" viewBox="0 0 1040 733" aria-hidden="true">
      <polygon class="logo-strip" points="522,504 976,504 968,557 506,557" fill="var(--white)"/>
    </svg>

    <h2 class="role-title">PERSONAL TRAINER</h2>
    <h1 class="trainer-name">MARCUS OFORI</h1>

    <h3 class="section-heading help-heading">HOW I CAN HELP YOU?</h3>
    <ul class="service-list">
      <li><span class="arrow">➡</span>Reduce body fat&nbsp; and increase body definition</li>
      <li><span class="arrow">➡</span>Increase stamina, improve agility and speed</li>
      <li><span class="arrow">➡</span>Increase strength and size</li>
      <li><span class="arrow">➡</span>Plyometric training and conditioning</li>
      <li><span class="arrow">➡</span>Flexibility and core strength</li>
    </ul>

    <h3 class="section-heading clients-heading">WHAT MY CLIENTS SAY ABOUT ME?</h3>
    <p class="client-quote">&nbsp;"With Marcus my training is always challenging and fun. I don’t remember a session to be boring or repetitive. In short time I improved my core strength and flexibility. I can run 10k without stopping. It is amazing improvement.&nbsp; " Laura Penhallow</p>

    <div class="brand-mark"><span class="brand-square"></span>Corbell Vitality</div>

    <h3 class="section-heading qualifications-heading">QUALIFICATIONS</h3>
    <ul class="qualification-list">
      <li><span class="dot">•</span>Advanced Circuit Training</li>
      <li><span class="dot">•</span>Advanced Diploma in Personal Training - Level 3 FPRB Registered</li>
      <li><span class="dot">•</span>Fitness Instructor - Level 2 FPRB Registered</li>
      <li><span class="dot">•</span>Also qualified in – Suspension training, Studio Cycling, Sports Nutrition, Weight Management</li>
    </ul>
  </section>
</body>
</html>
```